Hallo,
ich bin gerade dabei, ein ebook über alternative Heilmethoden für die Frauenkrankheit Endometriose zu schreiben. Dafür brauche ich ein ausdrucksstarkes Cover. Meine Zielgruppe sind dementsprechend Frauen, die Endometriose haben. Bei Endometriose wächst Schleimhaut aus der Gebärmutter im Bauchraum, den Eierstöcken usw. Symptome sind u.a. starke Schmerzen und Kinderlosigkeit. Die Krankheit ist schulmedizinisch nicht gut behandelbar und nicht heilbar, aber es gibt zahlreiche alternative Heilmethoden, die die Symptome lindern können. Darüber soll das Buch handeln. Hier die Website zum Buch: http://www.lindenblattwissen.de/
Vielen Dank und freundliche Grüße
Katrin Wollny
Das Cover soll eine positive Stimmung rüber bringen. So wie das Bild auf der Website. Leider darf ich das Bild nur für die Website verwenden.

```html
<!DOCTYPE html>
<html lang="de">
<head>
<meta charset="utf-8">
<title>Endometriose – lindern und leben · Coverentwürfe</title>
<link rel="stylesheet" href="https://fonts.googleapis.com/css2?family=Rajdhani:wght@300;400;500;600&display=swap">
<style>
  :root {
    --backdrop: #f4f4f4;
    --mint: #95d5ca;
    --crimson: #c8163c;
    --rose: #e23a60;
    --ink: #1f2d2b;
    --author: #4a5856;
    --white: #ffffff;
    --leaf-light: #e6eee0;
    --leaf-mid: #a9c495;
    --leaf-dark: #5f8a4f;
  }
  * { box-sizing: border-box; margin: 0; padding: 0; }
  html, body {
    width: 1200px; height: 851px; overflow: hidden;
    background: var(--backdrop);
  }
  .stage {
    width: 1200px; height: 851px;
    display: flex; justify-content: center; align-items: center; gap: 120px;
  }
  .cover {
    position: relative;
    width: 380px; height: 660px;
    background: var(--mint);
    font-family: "Rajdhani", "Arial Narrow", sans-serif;
    overflow: hidden;
    box-shadow: 0 10px 30px rgba(0,0,0,0.12);
  }
  .cover__author {
    position: absolute; left: 24px; top: 28px;
    font-size: 15px; font-weight: 500; color: var(--author);
    letter-spacing: 0.2px;
  }
  .cover__title {
    position: absolute; left: 0; right: 0;
    text-align: center;
    font-size: 47px; font-weight: 300; letter-spacing: 1.5px;
    line-height: 1;
  }
  .cover__subtitle {
    position: absolute; left: 0; right: 0;
    text-align: center;
    font-size: 43px; font-weight: 600; color: var(--white);
    letter-spacing: 0.5px; line-height: 1;
  }
  .cover__photo {
    position: absolute; left: 0; right: 0; bottom: 0;
    background:
      radial-gradient(ellipse 28% 22% at 30% 70%, rgba(200,22,60,0.75), transparent 70%),
      radial-gradient(ellipse 60% 50% at 70% 30%, var(--leaf-light), transparent 70%),
      radial-gradient(ellipse 50% 60% at 20% 20%, var(--leaf-mid), transparent 75%),
      linear-gradient(160deg, var(--leaf-light) 0%, var(--leaf-mid) 55%, var(--leaf-dark) 100%);
  }

  /* Variante A: rotes Band */
  .cover--band .cover__title { top: 90px; color: var(--ink); }
  .cover--band .band {
    position: absolute; left: 0; right: 0; top: 140px; height: 122px;
    background: var(--crimson);
  }
  .cover--band .cover__subtitle { top: 180px; }
  .cover--band .cover__photo { top: 262px; }

  /* Variante B: durchgehend Mint */
  .cover--mint .cover__title { top: 132px; color: var(--rose); }
  .cover--mint .cover__subtitle { top: 190px; }
  .cover--mint .rule {
    position: absolute; left: 0; right: 0; top: 246px; height: 4px;
    background: var(--white);
  }
  .cover--mint .cover__photo { top: 254px; }
</style>
</head>
<body>
<main class="stage">
  <article class="cover cover--band">
    <p class="cover__author">Katrin Wollny</p>
    <h1 class="cover__title">ENDOMETRIOSE</h1>
    <div class="band"></div>
    <p class="cover__subtitle">lindern und leben</p>
    <div class="cover__photo" role="img" aria-label="Foto: junge Frau im roten Kleid breitet vor blühenden Bäumen die Arme aus"></div>
  </article>

  <article class="cover cover--mint">
    <p class="cover__author">Katrin Wollny</p>
    <h1 class="cover__title">ENDOMETRIOSE</h1>
    <p class="cover__subtitle">lindern und leben</p>
    <div class="rule"></div>
    <div class="cover__photo" role="img" aria-label="Foto: junge Frau im roten Kleid breitet vor blühenden Bäumen die Arme aus"></div>
  </article>
</main>
</body>
</html>
```